Business Card Design Project

We need a Business Card for an Mechanical Engineering firm in Singapore. The design should be Modern & Technical looking, yet eye catching.

Our company deals in Cutting Tools & Machine Accessories for the Manufacturing Industries such as Oil & Gas, Aero Space, etc... For more information on our Company, you can either email me or view our website www.valtrion.com.sg.

We are trying to revamp our image to give our consumers a fresh new perspective to our company, so we welcome all ideas.

Industry/Entity Type

Business

Requirements
Must have
• Must incorporate New Company Logo into the card as shown in Uploaded file.

```html
<!DOCTYPE html>
<html lang="en">
<head>
<meta charset="utf-8">
<title>Valtrion Tools – Business Card</title>
<link href="https://fonts.googleapis.com/css2?family=Open+Sans:wght@400;600&family=Oswald:wght@300;400&display=swap" rel="stylesheet">
<style>
  :root {
    --crimson: #9b1a36;
    --ink: #2b2b2b;
    --paper: #f3f3f1;
    --backdrop: #d9d6d0;
  }
  * { margin: 0; padding: 0; box-sizing: border-box; }
  html, body { width: 1200px; height: 900px; overflow: hidden; }
  body {
    background: var(--backdrop);
    position: relative;
    font-family: "Open Sans", sans-serif;
    color: var(--ink);
  }
  .card {
    position: absolute;
    width: 560px;
    height: 320px;
    background: var(--paper);
    box-shadow: 0 6px 18px rgba(0,0,0,.18);
    overflow: hidden;
  }
  /* Front: logo side */
  .card--front { left: 580px; top: 90px; }
  .card--front .flags { position: absolute; inset: 0; }
  .brand {
    position: absolute;
    left: 0; right: 0; top: 124px;
    display: flex; align-items: center; justify-content: center; gap: 14px;
  }
  .brand__dot {
    width: 34px; height: 34px; border-radius: 50%;
    background: var(--crimson);
  }
  .brand__name {
    font-family: "Oswald", sans-serif;
    font-weight: 400;
    font-size: 48px;
    letter-spacing: 2px;
    color: var(--crimson);
    text-transform: uppercase;
  }
  /* Back: contact side */
  .card--back { left: 60px; top: 480px; }
  .card--back .band {
    position: absolute; left: 0; right: 0; bottom: 0; height: 58px;
    background: var(--crimson);
  }
  .contacts {
    position: absolute; left: 36px; top: 42px;
    list-style: none; font-size: 14px; line-height: 27px;
  }
  .contacts .label { color: var(--crimson); display: inline-block; width: 24px; }
  .identity { position: absolute; left: 318px; top: 36px; }
  .identity .brand-mini {
    display: flex; align-items: center; gap: 8px; margin-bottom: 10px;
  }
  .identity .brand-mini .brand__dot { width: 16px; height: 16px; }
  .identity .brand-mini .brand__name { font-size: 22px; letter-spacing: 1px; }
  .person__name {
    font-family: "Oswald", sans-serif; font-weight: 400;
    font-size: 22px; letter-spacing: 1px; text-transform: uppercase; line-height: 1.1;
  }
  .person__role {
    font-family: "Oswald", sans-serif; font-weight: 300;
    font-size: 13px; letter-spacing: 1px; text-transform: uppercase;
  }
  .address {
    position: absolute; left: 318px; top: 160px;
    font-size: 14px; line-height: 21px;
  }
  .address .label { color: var(--crimson); display: block; }
</style>
</head>
<body>

  <section class="card card--front" aria-label="Business card front">
    <svg class="flags" width="560" height="320" viewBox="0 0 560 320" aria-hidden="true">
      <polygon points="0,92 150,92 118,136 0,136" fill="var(--crimson)"/>
      <polygon points="560,196 442,196 410,240 560,240" fill="var(--crimson)"/>
    </svg>
    <div class="brand">
      <span class="brand__dot"></span>
      <span class="brand__name">Valtrion Tools</span>
    </div>
  </section>

  <section class="card card--back" aria-label="Business card back">
    <ul class="contacts">
      <li><span class="label">t :</span>6480 1127</li>
      <li><span class="label">f :</span>6480 1128</li>
      <li><span class="label">e :</span>daniel.whitmore@valtrion.com</li>
      <li><span class="label">w :</span>http://www.valtriontools.com</li>
    </ul>
    <div class="identity">
      <div class="brand-mini">
        <span class="brand__dot"></span>
        <span class="brand__name">Valtrion Tools</span>
      </div>
      <p class="person__name">Daniel Whitmore</p>
      <p class="person__role">Managing Director</p>
    </div>
    <address class="address" style="font-style:normal">
      <span class="label">a :</span>
      Blk 52 Kestrel Road<br>
      # 09-14 Kestrel Towers<br>
      SINGAPORE 309412
    </address>
    <div class="band"></div>
  </section>

</body>
</html>
```